Maple Glow Label

Design a label for new brand called Maple Glow. The specific product label :
Maple Glow Cocoa Butter Lotion. You only need to design the front label.
I have included the logo and a bottle jpeg with 2 bottles on it. Please try your best.

Requirements
Must have
• text on the label other than the logo:
cocoa butter
lotion
8.5oz/250ml

Original Moisturizing Formula
Smoothes Marks
Protect Skin

__________________________________
- ALTERNATIVE TEXT TO ALSO USE:
Smoothes Dry Skin, Blemishes & Stretch Marks
Softens Hands, Face and Body
Vitamin E

```html
<!DOCTYPE html>
<html lang="en">
<head>
<meta charset="utf-8">
<title>Maple Glow Cocoa Butter Lotion – Front Label</title>
<link rel="stylesheet" href="https://fonts.googleapis.com/css2?family=Cormorant+SC:wght@600&family=Great+Vibes&family=Open+Sans:wght@400&display=swap">
<style>
  :root {
    --page-bg: #ffffff;
    --label-top: #dcedf3;
    --label-mid: #bfe3e0;
    --label-bottom: #8fd0b9;
    --ink-dark: #2c3a3a;
    --script-pink: #e9707d;
    --leaf-green: #4fa63a;
    --muted-grey: #7d8d8c;
    --flower-pink: rgba(214, 150, 150, 0.45);
    --flower-mint: rgba(240, 250, 245, 0.55);
  }
  html, body {
    margin: 0;
    padding: 0;
    width: 777px;
    height: 1200px;
    overflow: hidden;
    background: var(--page-bg);
  }
  .canvas {
    position: relative;
    width: 777px;
    height: 1200px;
  }
  .label {
    position: absolute;
    left: 48px;
    top: 85px;
    width: 680px;
    height: 1030px;
    border-radius: 150px / 170px;
    overflow: hidden;
    background: linear-gradient(180deg, var(--label-top) 0%, var(--label-mid) 50%, var(--label-bottom) 100%);
    box-shadow: 0 0 0 1px rgba(0,0,0,0.06);
  }
  .floral {
    position: absolute;
    border-radius: 50%;
  }
  .floral--upper-left {
    left: -40px; top: 160px; width: 300px; height: 260px;
    background: radial-gradient(circle at 45% 50%, var(--flower-pink) 0%, var(--flower-mint) 45%, transparent 72%);
  }
  .floral--right {
    right: -60px; top: 560px; width: 280px; height: 380px;
    background: radial-gradient(circle at 50% 45%, var(--flower-pink) 0%, var(--flower-mint) 40%, transparent 72%);
  }
  .floral--lower-left {
    left: -50px; bottom: -20px; width: 300px; height: 300px;
    background: radial-gradient(circle at 45% 45%, var(--flower-pink) 0%, var(--flower-mint) 42%, transparent 72%);
  }
  .brand-name {
    position: absolute;
    top: 70px;
    left: 0; right: 0;
    text-align: center;
    font-family: "Cormorant SC", serif;
    font-weight: 600;
    font-size: 76px;
    color: var(--ink-dark);
    margin: 0;
  }
  .product-name {
    position: absolute;
    top: 255px;
    left: 0; right: 0;
    margin: 0;
    text-align: center;
    font-family: "Great Vibes", cursive;
    font-weight: 400;
    color: var(--script-pink);
    line-height: 1;
  }
  .product-name__main { display: block; font-size: 118px; }
  .product-name__sub { display: block; font-size: 104px; margin-top: 8px; }
  .claims {
    position: absolute;
    top: 520px;
    left: 50px;
    margin: 0;
    padding: 0;
    list-style: none;
    font-family: "Cormorant SC", serif;
    font-weight: 600;
    font-size: 36px;
    line-height: 44px;
    color: var(--ink-dark);
  }
  .benefits {
    position: absolute;
    top: 680px;
    left: 50px;
    margin: 0;
    padding: 0;
    list-style: none;
    font-family: "Open Sans", sans-serif;
    font-size: 19px;
    line-height: 27px;
    color: var(--leaf-green);
  }
  .net-volume {
    position: absolute;
    top: 948px;
    left: 0; right: 0;
    text-align: center;
    font-family: "Open Sans", sans-serif;
    font-size: 17px;
    color: var(--muted-grey);
    margin: 0;
  }
</style>
</head>
<body>
  <main class="canvas">
    <section class="label">
      <div class="floral floral--upper-left" role="img" aria-label="Pastel line-drawn flowers and swirling vines"></div>
      <div class="floral floral--right" role="img" aria-label="Pastel line-drawn flowers along the right edge"></div>
      <div class="floral floral--lower-left" role="img" aria-label="Pastel line-drawn flowers in the lower corner"></div>

      <p class="brand-name">Maple Glow</p>

      <h1 class="product-name">
        <span class="product-name__main">Cocoa Butter</span>
        <span class="product-name__sub">lotion</span>
      </h1>

      <ul class="claims">
        <li>Original Moisturizing Formula</li>
        <li>Smoothes Marks</li>
        <li>Protect Skin</li>
      </ul>

      <ul class="benefits">
        <li>Smoothes Dry Skin, Blemishes &amp; Stretch Marks</li>
        <li>Softens Hands, Face and Body</li>
        <li>Vitamin E</li>
      </ul>

      <p class="net-volume">8.5oz/250ml</p>
    </section>
  </main>
</body>
</html>
```